I have an existing corporate logo. I'd like to clean it up bit (sharpen it up) and make it look better (without major redesign). I'd like to get the logo itself in all major file formats for print, web, etc.
Then I'd like a business card design that reflects a strategy consulting firm. It should be clean - logo and text without major graphics, and perhaps some small color treatments that match the logo color. The card should suggest high quality in terms of the company.
I'd like the files for card in all major print formats.
Target Market(s)
Silver Birch Partners is a strategy development and business consulting firm focused on small to mid-sized companies. We specialize in business strategy, comprehensive business plan development, market segmentation and positioning, financial models, marketing and sales strategy, product strategy and the effective use of social media in business growth. We operate as consultants, advisers, retained members of management teams, and Board members. We often serve in the role of Chief Strategy Officer, supporting CEO's and other senior executives to enhance top and bottom line growth.
Our overall approach with clients is to deliver actual results, and we often take an active team role with business founders and management teams to drive business growth and affect real changes in performance. As a result, we approach each situation uniquely and partner with clients in a manner that will have the biggest impact on enterprise value.
Industry/Entity Type
Business
Look and feel

```html
<!DOCTYPE html>
<html lang="en">
<head>
<meta charset="utf-8">
<title>Silver Birch Partners – Business Card</title>
<link href="https://fonts.googleapis.com/css2?family=Lato:wght@400;700;900&display=swap" rel="stylesheet">
<style>
  :root {
    --navy: #232f5f;
    --gold: #d9a72a;
    --paper: #ffffff;
    --backdrop: #e9e9ea;
  }
  * { margin: 0; padding: 0; box-sizing: border-box; }
  html, body {
    width: 1200px;
    height: 1000px;
    overflow: hidden;
    background: var(--backdrop);
    font-family: "Lato", Arial, sans-serif;
  }
  .business-card {
    position: absolute;
    left: 251px;
    top: 285px;
    width: 698px;
    height: 430px;
    background: var(--paper);
    overflow: hidden;
    box-shadow: 0 2px 6px rgba(0, 0, 0, 0.18);
  }
  .company-name {
    position: absolute;
    left: 40px;
    top: 84px;
    color: var(--navy);
    font-weight: 900;
    font-size: 27px;
    line-height: 38px;
    letter-spacing: 1.5px;
    text-transform: uppercase;
  }
  .contact-block {
    position: absolute;
    left: 412px;
    top: 48px;
    color: var(--navy);
  }
  .person-name {
    color: var(--gold);
    font-weight: 700;
    font-size: 24px;
    line-height: 30px;
  }
  .person-title {
    font-size: 16px;
    font-weight: 400;
    line-height: 22px;
  }
  .address {
    margin-top: 24px;
    font-size: 16px;
    font-weight: 400;
    line-height: 26px;
  }
  .contact-list {
    list-style: none;
    margin-top: 30px;
  }
  .contact-list li {
    display: flex;
    align-items: center;
    height: 26px;
    font-size: 16px;
    font-weight: 400;
  }
  .contact-icon {
    width: 18px;
    height: 18px;
    margin-right: 11px;
    flex-shrink: 0;
  }
  .contact-icon .fill { fill: var(--gold); }
  .contact-icon .stroke { fill: none; stroke: var(--gold); stroke-width: 2; }
  .footer-rule {
    position: absolute;
    left: 0;
    bottom: 30px;
    width: 100%;
    height: 6px;
    background: var(--gold);
  }
  .footer-band {
    position: absolute;
    left: 0;
    bottom: 0;
    width: 100%;
    height: 30px;
    background: var(--navy);
  }
</style>
</head>
<body>
  <main class="business-card">
    <div class="company-name">Silver Birch<br>Partners, LLC</div>

    <section class="contact-block">
      <div class="person-name">Daniel K. Mercer</div>
      <div class="person-title">Partner and Founder</div>
      <div class="address">412 Alder Court<br>Fairview, Illinois 60510</div>
      <ul class="contact-list">
        <li>
          <svg class="contact-icon" viewBox="0 0 18 18" aria-hidden="true">
            <path class="fill" d="M3.5 1.5l3 .4 1.2 3.6-1.9 1.4c.9 1.9 2.4 3.4 4.3 4.3l1.4-1.9 3.6 1.2.4 3c-.2 1-1 1.6-2 1.6C7.5 15.1 2.9 10.5 1.9 4.5c0-1 .6-2.8 1.6-3z"/>
          </svg>
          312.555.0148
        </li>
        <li>
          <svg class="contact-icon" viewBox="0 0 18 18" aria-hidden="true">
            <path class="fill" d="M1 4h16v1.2L9 10 1 5.2z"/>
            <path class="fill" d="M1 6.8l8 4.8 8-4.8V14H1z"/>
          </svg>
          dan@sbpartners.com
        </li>
        <li>
          <svg class="contact-icon" viewBox="0 0 18 18" aria-hidden="true">
            <circle class="stroke" cx="9" cy="9" r="7.5"/>
            <path class="stroke" d="M1.5 9h15M9 1.5c-3 3.5-3 11.5 0 15M9 1.5c3 3.5 3 11.5 0 15"/>
          </svg>
          www.sbpartners.com
        </li>
        <li>
          <svg class="contact-icon" viewBox="0 0 18 18" aria-hidden="true">
            <rect class="fill" x="1.5" y="1.5" width="15" height="15" rx="1.5"/>
          </svg>
          profilehub.net/in/dkmercer/
        </li>
        <li>
          <svg class="contact-icon" viewBox="0 0 18 18" aria-hidden="true">
            <circle class="fill" cx="9" cy="9" r="7.5"/>
          </svg>
          DanMercer
        </li>
      </ul>
    </section>

    <div class="footer-rule"></div>
    <div class="footer-band"></div>
  </main>
</body>
</html>
```